Letterhead creation for military law attorney

I need letterhead design for my business. We are now only doing military law and need to change address, logo and vision. I like the idea of using an eagle or a jolly roger flag

Target Market(s)

Military Law Clients

Colors
3176b5
85abd2

Requirements
Must have
• We are defending people against the government
Nice to have
• Jolly Roger Flag

```html
<!DOCTYPE html>
<html lang="en">
<head>
<meta charset="utf-8">
<title>Garrison Law PLLC — Letterhead</title>
<link rel="stylesheet" href="https://fonts.googleapis.com/css2?family=Arimo:ital,wght@0,400;0,700;1,400;1,700&display=swap">
<style>
  :root {
    --backdrop: #d8d9dd;
    --paper: #fafafa;
    --ink: #1e1e1e;
    --ink-soft: #2c2c2c;
    --brand-blue: #3176b5;
    --brand-blue-light: #85abd2;
    --sign-fill: #e3ecf5;
  }
  * { margin: 0; padding: 0; box-sizing: border-box; }
  html, body {
    width: 1200px; height: 1166px; overflow: hidden;
    background: var(--backdrop);
    font-family: "Arimo", Arial, sans-serif;
    color: var(--ink);
  }
  .letterhead {
    position: absolute; left: 228px; top: 104px;
    width: 742px; height: 958px;
    background: var(--paper);
  }
  .brand {
    position: absolute; left: 69px; top: 58px;
    display: flex; align-items: center; gap: 14px;
  }
  .brand-square {
    width: 58px; height: 58px;
    background: var(--brand-blue);
    border-right: 10px solid var(--brand-blue-light);
  }
  .brand-name {
    font-weight: 700; font-size: 28px; line-height: 27px;
    letter-spacing: -0.6px; color: var(--brand-blue);
  }
  .sender {
    position: absolute; right: 65px; top: 57px;
    text-align: right; font-style: italic;
    font-size: 9.8px; line-height: 15.4px; color: var(--ink-soft);
  }
  .sender .firm { font-weight: 700; color: var(--brand-blue); }
  .sender .web b { font-weight: 700; color: var(--brand-blue); }
  .recipient {
    position: absolute; left: 66px; top: 255px;
    font-style: normal;
    font-size: 10.4px; line-height: 12.9px; color: var(--ink-soft);
  }
  .body {
    position: absolute; left: 66px; top: 362px; width: 611px;
    font-size: 9.9px; line-height: 12.9px; text-align: justify;
    color: var(--ink-soft);
  }
  .salutation { font-weight: 700; font-size: 10.4px; margin-bottom: 12px; color: var(--ink); }
  .body p { margin-bottom: 12.8px; }
  .closing {
    position: absolute; left: 66px; top: 684px;
    font-size: 10.4px; line-height: 12.9px; color: var(--ink-soft);
  }
  .signature {
    width: 128px; height: 48px; margin: 12px 0 18px;
    background: var(--sign-fill); border-radius: 24px;
  }
  .signer-name { font-weight: 700; color: var(--brand-blue); }
</style>
</head>
<body>
  <main class="letterhead">
    <header>
      <div class="brand">
        <span class="brand-square"></span>
        <span class="brand-name">GARRISON<br>LAW PLLC</span>
      </div>
      <address class="sender">
        <div class="firm">GARRISON LAW, PLLC</div>
        <div>PO Box 318, Fairhaven, TN 37900</div>
        <div>Tel: (555) 014-2260 · Fax: (555) 014-2261</div>
        <div class="web">www.<b>garrisonlaw</b>.example</div>
      </address>
    </header>

    <address class="recipient">
      Mr. Leonard Ashby<br>
      President and CEO<br>
      Northwind Labs LLC.<br>
      200 Harbor Street, Suite 1200<br>
      Riverton, NY 10990
    </address>

    <section class="body">
      <div class="salutation">Dear Mr. Ashby:</div>
      <p>As Chairperson of the Corporate Conscience Campaign - Helping the Homeless in Riverton, I am writing this to thank you personally for your company's support in last month's fund-raising effort.</p>
      <p>As I indicated when we spoke on the phone two weeks ago, the campaign was considered a resounding success, raising a total of $1.65 million to-date, significantly exceeding our target of $1 million. Some donations are still trickling in, so we could end up close to a total of $2 million.</p>
      <p>Northwind Labs was an influential leader throughout the entire three-month campaign. In fact, we couldn't have succeeded without the generous support of your company, both financially, and through your organizational and administrative assistance. Your Team Leader, Maren Holt was particularly impressive, going above and beyond what we could have expected of someone performing as a volunteer while continuing on with her day-to-day duties. Please convey my special thanks to Maren.</p>
      <p>I would also ask you to convey my sincere thanks and congratulations to all of those other people in your company who contributed in any way to the Helping the Homeless Campaign. Please tell them that the sum of their contributions resulted in a major success that they should all be proud of taking part in.</p>
      <p>I believe that the 27 companies that participated in this effort have set a new standard for social responsibility in this community, and have set a powerful example that will inspire other companies and organizations to do the same.</p>
      <p>I look forward to seeing you at the Mayor's special thank you reception next month.</p>
    </section>

    <footer class="closing">
      <div>Yours sincerely,</div>
      <div class="signature" role="img" aria-label="Handwritten signature of Daniel Reyes"></div>
      <div class="signer-name">Daniel Reyes</div>
      <div>Fundraising Chair</div>
    </footer>
  </main>
</body>
</html>
```